stationary for hygienic company

We need a stationary design for hygienic company which provides public high end sanitary products and high end public lavatory.
We need a fresh and clean style stationary
we want the following things:
* logo (redesigned in eps/vector)
* Letterhead (with company details)
* letterhead (without company details)
* Business card
* note block
* ballpoint
* etcetera (a complete package)

```html
<!DOCTYPE html>
<html lang="en">
<head>
<meta charset="utf-8">
<title>Lumiva Stationery – Letterhead and Folder</title>
<link href="https://fonts.googleapis.com/css2?family=Open+Sans:wght@400;600&display=swap" rel="stylesheet">
<style>
  :root {
    --backdrop: #e4e4e4;
    --paper: #fbfbfa;
    --ink: #1d1d1d;
    --ink-soft: #4a4a4a;
    --sky: #74c5e0;
    --mint: #6cc5a6;
    --green: #6ebf6c;
    --sun: #f6c84a;
    --orange: #f0894c;
    --red: #e84a48;
    --pink: #e4579a;
    --violet: #8a5aa6;
    --shadow: 0 14px 30px rgba(0,0,0,0.16);
  }
  * { box-sizing: border-box; margin: 0; padding: 0; }
  html, body {
    width: 1200px; height: 1000px; overflow: hidden;
    background: var(--backdrop);
    font-family: "Open Sans", Arial, sans-serif;
    color: var(--ink);
  }
  .stationery-set {
    position: relative; width: 1200px; height: 1000px;
  }
  .sheet {
    position: absolute; top: 150px;
    width: 480px; height: 680px;
    background: var(--paper);
    box-shadow: var(--shadow);
    overflow: hidden;
  }
  .letterhead { left: 80px; }
  .folder-cover { left: 640px; }

  /* brand block */
  .brand {
    position: absolute;
    display: flex; flex-direction: column; align-items: center;
    text-align: center;
  }
  .brand-row { display: flex; align-items: center; gap: 6px; }
  .brand-dot {
    width: 16px; height: 16px; border-radius: 50%;
    background: var(--pink);
  }
  .brand-name {
    font-size: 22px; font-weight: 600; color: var(--ink);
    letter-spacing: 0.5px; line-height: 1;
  }
  .brand-tagline {
    margin-top: 5px; font-size: 8.5px; font-weight: 600; color: var(--ink);
  }
  .letterhead .brand { top: 44px; left: 0; right: 0; }
  .folder-cover .brand { right: 24px; bottom: 34px; }

  /* letterhead footer */
  .contact-details {
    position: absolute; right: 26px; bottom: 82px;
    font-size: 8px; color: var(--ink-soft);
    display: flex; flex-direction: column; align-items: flex-end; gap: 4px;
  }
  .contact-line { display: flex; gap: 10px; align-items: center; }
  .contact-item { display: inline-flex; align-items: center; gap: 3px; }
  .contact-item svg { width: 8px; height: 8px; fill: var(--sky); }
  .footer-band {
    position: absolute; left: 0; right: 0; bottom: 0; height: 62px;
    background: linear-gradient(90deg, var(--pink), var(--mint) 22%, var(--orange) 45%, var(--sun) 65%, var(--sky) 85%, var(--mint));
    opacity: 0.9;
  }

  /* folder cover */
  .cover-pattern {
    position: absolute; left: -250px; top: 20px;
    width: 570px; height: 570px; border-radius: 50%;
    background: radial-gradient(circle at 50% 50%,
      var(--sky) 0 30%, var(--sun) 34%, var(--orange) 44%,
      var(--mint) 54%, var(--red) 66%, var(--violet) 80%, var(--pink) 100%);
  }
  .cover-spine {
    position: absolute; left: 0; top: 0; bottom: 0; width: 5px;
    background: linear-gradient(180deg, var(--pink), var(--violet), var(--sky), var(--red), var(--pink));
  }
</style>
</head>
<body>
<main class="stationery-set">

  <section class="sheet letterhead" aria-label="Letterhead">
    <div class="brand">
      <div class="brand-row">
        <span class="brand-dot"></span>
        <span class="brand-name">Lumiva</span>
      </div>
      <span class="brand-tagline">Boutique Hygiènique</span>
    </div>

    <address class="contact-details">
      <span class="contact-line">
        <span class="contact-item">
          <svg viewBox="0 0 10 10"><path d="M5 0a3.5 3.5 0 0 0-3.5 3.5C1.5 6 5 10 5 10s3.5-4 3.5-6.5A3.5 3.5 0 0 0 5 0zm0 5a1.5 1.5 0 1 1 0-3 1.5 1.5 0 0 1 0 3z"/></svg>
          123, Main Street, Anytown, Postal Code
        </span>
      </span>
      <span class="contact-line">
        <span class="contact-item">
          <svg viewBox="0 0 10 10"><path d="M2 0l2 2.5-1 1.2a6 6 0 0 0 3.3 3.3l1.2-1L10 8l-1.5 2C4 10 0 6 0 1.5z"/></svg>
          555-1234-56
        </span>
        <span class="contact-item">
          <svg viewBox="0 0 10 10"><rect x="0" y="1" width="10" height="8" rx="1"/></svg>
          555-1234-56
        </span>
        <span class="contact-item">
          <svg viewBox="0 0 10 10"><path d="M0 2h10v6H0zM0 2l5 3.5L10 2" /></svg>
          we@youraddress.com
        </span>
      </span>
    </address>

    <div class="footer-band" role="img" aria-label="Colourful mosaic pattern band"></div>
  </section>

  <section class="sheet folder-cover" aria-label="Presentation folder cover">
    <div class="cover-spine"></div>
    <div class="cover-pattern" role="img" aria-label="Large colourful mosaic half-flower pattern"></div>
    <div class="brand">
      <div class="brand-row">
        <span class="brand-dot"></span>
        <span class="brand-name">Lumiva</span>
      </div>
      <span class="brand-tagline">Boutique Hygiènique</span>
    </div>
  </section>

</main>
</body>
</html>
```